Zielgruppe
Pizzeria Restaurant. Zielgruppe sind Familien, Geschäftsleute, Beamter, Arbeiter, Pärchen, Schüler...
Aufgabenstellung
Das Restaurant wird mit ca. zwanzig Sitzplätzen erweitert. Die professionelle Aufmachung der Speisekarte hinterlässt einen positiven Eindruck bei den Gästen und lässt auf eine qualitativ hochwertige Küche schließen. Ich möchte ein schlichtes, dennoch modernes und edles Layout.
• Format: DIN A4, als Magazin mit Rückendrahtheftung
• Sparte bzw. kleiner Rahmen links oder rechts soll auf jeder Seite formatiert sein, um die Geschichte/ das Thema einzufügen
• „Datei Enzo seit 2003“ kann jeweils auf jeder Seite unterhalb den Sparten eingefügt werden (wo die Geschichten/ Themen zu lesen sein werden)
Die Fotos sind nur ein persönlicher Vorschlag. Sie können natürlich andere Bilder und Grafiken verwenden. Jedoch will ich zum Ausdruck bringen, dass ich ein einfaches Design bevorzuge und mehr auf die Klarheit des geschriebenen Inhaltes (Gerichte, Zutaten, Preisliste) wert lege. Ich freue mich auf Ihre Entwürfe und wünsche Ihnen viel Spaß bei der Gestaltung der Speisekarte.
MfG
Lorenzo

```html
<!DOCTYPE html>
<html lang="de">
<head>
<meta charset="utf-8">
<title>Lorenzo Speisekarte</title>
<link href="https://fonts.googleapis.com/css2?family=Open+Sans:ital,wght@0,400;0,600;0,700;1,400;1,700&family=Pinyon+Script&display=swap" rel="stylesheet">
<style>
:root{
  --wine:#6b1414;
  --paper:#ffffff;
  --ink:#222222;
  --muted:#555555;
  --backdrop:#d4d4d4;
  --sketch-light:#e2e2e2;
}
*{margin:0;padding:0;box-sizing:border-box}
html,body{width:1200px;height:2517px;overflow:hidden}
body{background:var(--backdrop);font-family:"Open Sans",Arial,sans-serif;color:var(--ink);position:relative}
.cover,.page{position:absolute;background:var(--paper);overflow:hidden}
.cover{left:367px;top:83px;width:445px;height:635px}
.cover-top{position:absolute;left:0;top:0;width:100%;height:154px;background:var(--wine)}
.cover-brand{position:absolute;top:190px;left:0;width:100%;text-align:center}
.brand-name{font-family:"Open Sans",sans-serif;font-weight:600;color:var(--wine);font-size:38px;line-height:1;letter-spacing:1px}
.cover-slogan{position:absolute;top:278px;left:0;width:100%;height:24px;background:var(--wine);color:#fff;font-size:12px;font-style:italic;text-align:center;line-height:24px}
.cover-label{position:absolute;left:96px;top:347px;width:252px;height:78px;border:3px solid var(--wine);display:flex;align-items:center;justify-content:center;font-family:"Pinyon Script",cursive;color:var(--wine);font-size:22px}
.illus{position:absolute;background:radial-gradient(circle at 50% 50%,var(--sketch-light),rgba(255,255,255,0))}
.illus.round{border-radius:50%;background:radial-gradient(circle,#9a9a9a 0%,#d0d0d0 55%,#f0f0f0 100%)}
.page{width:504px;height:752px}
.page-title{position:absolute;top:26px;left:0;width:100%;text-align:center;font-family:"Pinyon Script",cursive;font-weight:400;color:var(--wine);font-size:26px}
.page-title .sep{font-family:"Open Sans",sans-serif;font-size:10px;font-weight:700;margin:0 10px;vertical-align:4px}
.footer-band{position:absolute;left:0;bottom:0;width:100%;height:77px;background:var(--wine);display:flex;align-items:center;justify-content:center}
.footer-band .brand-name{color:#fff;font-size:18px}
.menu-box{position:absolute;border:3px solid var(--wine);background:#fff;padding:18px 20px 10px 20px}
.box-title{font-size:13px;font-weight:600;letter-spacing:.3px;margin-bottom:12px;text-transform:uppercase}
.box-title.next{margin-top:18px}
.dish{display:flex;justify-content:space-between;align-items:flex-end;margin-bottom:8px}
.dish-name{font-size:8.5px;font-weight:700;text-transform:uppercase;line-height:1.2}
.dish-desc{display:block;font-size:8px;font-style:italic;font-weight:400;text-transform:none;color:var(--muted)}
.price{font-size:9px;font-style:italic;font-weight:700;color:var(--wine);flex:none;margin-left:8px}
.story-box{position:absolute;background:var(--wine);color:#fff;padding:18px 22px}
.story-head{display:flex;justify-content:space-between;align-items:baseline;margin-bottom:14px}
.story-title{font-size:13px;font-weight:600;letter-spacing:.5px}
.story-since{font-size:8px;font-weight:400}
.story-text{font-size:8.5px;line-height:1.55}
</style>
</head>
<body>

<section class="cover">
  <div class="cover-top"></div>
  <div class="cover-brand"><span class="brand-name">Lorenzo</span></div>
  <div class="cover-slogan">Das Original. Schmeckt besser</div>
  <div class="cover-label">Speisekarte</div>
  <div class="illus" style="left:280px;top:327px;width:165px;height:245px" role="img" aria-label="Zeichnung eines Olivenzweigs"></div>
</section>

<section class="page" style="left:100px;top:828px">
  <h2 class="page-title">Antipasti<span class="sep">··</span>Vorspeisen</h2>
  <div class="menu-box" style="left:50px;top:92px;width:195px;height:177px">
    <h3 class="box-title">Kalte Vorspeisen</h3>
    <div class="dish"><span class="dish-name">Mozzarella<br>Con-Pomodore</span><span class="price">5,50</span></div>
    <div class="dish"><span class="dish-name">Cocktail di Gamberetti</span><span class="price">5,50</span></div>
    <div class="dish"><span class="dish-name">Carpaccio</span><span class="price">5,50</span></div>
    <div class="dish"><span class="dish-name">Tzatziki</span><span class="price">5,50</span></div>
    <div class="dish"><span class="dish-name">Mezes</span><span class="price">5,50</span></div>
  </div>
  <div class="menu-box" style="left:257px;top:92px;width:195px;height:177px">
    <h3 class="box-title">Suppen</h3>
    <div class="dish"><span class="dish-name">Zuppa di Pomodoro<span class="dish-desc">Tomatensuppe mit<br>Schlagobers</span></span><span class="price">5,50</span></div>
    <div class="dish"><span class="dish-name">Zuppa con Aglio<span class="dish-desc">Knoblauchsuppe</span></span><span class="price">5,50</span></div>
    <div class="dish"><span class="dish-name">Zuppa di Cipolle<span class="dish-desc">Zwiebelsuppe</span></span><span class="price">5,50</span></div>
  </div>
  <div class="menu-box" style="left:50px;top:282px;width:330px;height:148px;padding-right:80px">
    <h3 class="box-title">Warme Vorspeisen</h3>
    <div class="dish"><span class="dish-name">Saganaki</span><span class="price">5,50</span></div>
    <div class="dish"><span class="dish-name">Shrimps Saganaki</span><span class="price">5,50</span></div>
    <div class="dish"><span class="dish-name">Cozze al Vino Bianco<span class="dish-desc">Miesmuscheln in Weißwein- oder<br>Tomaten-sauce mit Pizzabrot</span></span><span class="price">5,50</span></div>
  </div>
  <div class="illus round" style="left:318px;top:262px;width:172px;height:172px" role="img" aria-label="Zeichnung einer Schale mit Oliven"></div>
  <div class="illus" style="left:0;top:415px;width:270px;height:260px" role="img" aria-label="Zeichnung einer geschnittenen Salami"></div>
  <div class="story-box" style="left:255px;top:502px;width:197px;height:148px">
    <div class="story-head"><h3 class="story-title">GESCHICHTE</h3><span class="story-since">Enzo seit 2003</span></div>
    <p class="story-text">Me estianihit volo ditiissit verum eum veles dolupta volorate dem que porum es etur aut experiate perchic to eturita quiat. Faccuptat officius-dae et untis apiet as</p>
  </div>
  <footer class="footer-band"><span class="brand-name">Lorenzo</span></footer>
</section>

<section class="page" style="left:604px;top:828px">
  <h2 class="page-title">Insalata<span class="sep">··</span>Salate</h2>
  <div class="illus" style="left:350px;top:0;width:154px;height:130px" role="img" aria-label="Zeichnung von Rispentomaten"></div>
  <div class="story-box" style="left:42px;top:92px;width:196px;height:164px">
    <div class="story-head"><h3 class="story-title">GESCHICHTE</h3><span class="story-since">Enzo seit 2003</span></div>
    <p class="story-text">Me estianihit volo ditiissit verum eum veles dolupta volorate dem que porum es etur aut experiate perchic to eturita quiat. Faccuptat officius-dae et untis apiet as To eles et ad ma inctiusci blant, inctio.</p>
  </div>
  <div class="menu-box" style="left:252px;top:90px;width:196px;height:166px">
    <h3 class="box-title">Salate</h3>
    <div class="dish"><span class="dish-name">Insalata Verde</span><span class="price">5,50</span></div>
    <div class="dish"><span class="dish-name">Insalata Mista</span><span class="price">5,50</span></div>
    <div class="dish"><span class="dish-name">Insalata Grece</span><span class="price">5,50</span></div>
    <div class="dish"><span class="dish-name">Insalata di Tonno</span><span class="price">5,50</span></div>
    <div class="dish"><span class="dish-name">Insalata di Pollo</span><span class="price">5,50</span></div>
  </div>
  <div class="menu-box" style="left:42px;top:268px;width:405px;height:294px">
    <h3 class="box-title">Al Forno / Überbacken</h3>
    <div class="dish"><span class="dish-name">Lasagne al Forno<span class="dish-desc">Gefüllte Teigblätter mit Fleischsauce &amp; Käse überbacken</span></span><span class="price">6,90</span></div>
    <div class="dish"><span class="dish-name">Broccoli al Forno<span class="dish-desc">Broccoli mit Schinken, Knoblauch und Käse überbacken</span></span><span class="price">6,90</span></div>
    <div class="dish"><span class="dish-name">Mussaka al Forno<span class="dish-desc">Backofengericht aus Melanzane, faschiertem Fleisch,<br>Kartoffeln, geriebenem Käse und Bechamel</span></span><span class="price">7,20</span></div>
    <div class="dish"><span class="dish-name">Verdura Fantastico<span class="dish-desc">Melanzani, Zucchini, Broccoli, Paprika,<br>mit Käse überbacken</span></span><span class="price">7,20</span></div>
    <div class="dish" style="width:200px"><span class="dish-name">Tortellini al Forno<span class="dish-desc">mit Schinken, Oberssauce<br>und Käse überbacken</span></span><span class="price">7,20</span></div>
    <div class="dish" style="width:200px"><span class="dish-name">Maccaroni al Forno<span class="dish-desc">mit Schinken, Oberssauce<br>und Käse überbacken</span></span><span class="price">7,20</span></div>
  </div>
  <div class="illus" style="left:265px;top:480px;width:239px;height:210px" role="img" aria-label="Zeichnung eines Stücks Lasagne mit Basilikum"></div>
  <footer class="footer-band"><span class="brand-name">Lorenzo</span></footer>
</section>

<section class="page" style="left:100px;top:1680px">
  <h2 class="page-title">Secondi di Pesce<span class="sep">··</span>Fisch</h2>
  <div class="menu-box" style="left:48px;top:88px;width:407px;height:316px;padding-right:50px">
    <h3 class="box-title">Pesce (Fisch)</h3>
    <div class="dish"><span class="dish-name">Sogliola Fritta<span class="dish-desc">Scholle gebacken mit Bratkartoffel und Sauce Tartar</span></span><span class="price">7,50</span></div>
    <div class="dish"><span class="dish-name">Scampi Fritti<span class="dish-desc">Garnelen in Bierteig gebacken mit Petersilkartoffel &amp; Sauce Tartar</span></span><span class="price">12,50</span></div>
    <h3 class="box-title next">Pesce alla Griglia (Fisch vom Grill)</h3>
    <div class="dish" style="margin-right:-30px"><span class="dish-name">Solea alla Griglia<span class="dish-desc">Seezunge gegrillt mit Knoblauchsauce und Petersilkartoffel</span></span><span class="price">9,20</span></div>
    <div class="dish" style="margin-right:-30px"><span class="dish-name">Halibut<span class="dish-desc">Heilbutt gegrillt mit Knoblauchsauce und Petersilkartoffel</span></span><span class="price">9,50</span></div>
    <div class="dish" style="margin-right:-30px"><span class="dish-name">Calamari alla Griglia<span class="dish-desc">Tintenfisch gegrillt mit Knoblauchsauce und Reis</span></span><span class="price">9,50</span></div>
    <div class="dish" style="margin-right:-30px"><span class="dish-name">Scampi alla Griglia<span class="dish-desc">Garnelen gegrillt ohne Schale mit Knoblauchsauce und Reis</span></span><span class="price">13,80</span></div>
  </div>
  <div class="illus round" style="left:405px;top:110px;width:135px;height:135px" role="img" aria-label="Zeichnung einer Zitronenscheibe"></div>
  <div class="story-box" style="left:48px;top:415px;width:197px;height:240px">
    <div class="story-head"><h3 class="story-title">GESCHICHTE</h3><span class="story-since">Enzo seit 2003</span></div>
    <p class="story-text">Me estianihit volo ditiissit verum eum veles dolupta volorate dem que porum es etur aut experiate perchic to eturita quiat. Faccuptat officiusdae et untis apiet as To eles et ad ma inctiusci blant, inctio. Imaximposam am, corest venimin consequissit as esti ni incta cor auda ditiae. Et expliti untorem quatect emporit, vollab iur, sitati .</p>
  </div>
  <div class="illus" style="left:0;top:500px;width:95px;height:110px" role="img" aria-label="Zeichnung eines Zitronenviertels"></div>
  <div class="illus" style="left:310px;top:350px;width:170px;height:300px" role="img" aria-label="Zeichnung von Garnelen"></div>
  <footer class="footer-band"><span class="brand-name">Lorenzo</span></footer>
</section>

<section class="page" style="left:604px;top:1680px">
  <h2 class="page-title">Secondi di Carne<span class="sep">··</span>Fleisch</h2>
  <div class="menu-box" style="left:40px;top:92px;width:408px;height:210px">
    <h3 class="box-title">Secondi di Carne</h3>
    <div class="dish"><span class="dish-name">Costoletta alla Griglia<span class="dish-desc">Schweinskotelette gegrillt mit Pommes, Reis und Naturgemüse</span></span><span class="price">8,80</span></div>
    <div class="dish"><span class="dish-name">Scaloppine Veronese<span class="dish-desc">Naturschnitzel in Weinsauce mit Schinken, Käse überbacken,<br>Reis oder Bratkartoffel</span></span><span class="price">9,20</span></div>
    <div class="dish"><span class="dish-name">Pollo al Funghi<span class="dish-desc">Hähnchenbrust in Wein-Obers-Sauce mit Champignons.</span></span><span class="price">8,80</span></div>
    <div class="dish"><span class="dish-name">Scaloppine alla Milanese<span class="dish-desc">Schweinsschnitzel nach Wiener Art mit Pommes</span></span><span class="price">8,20</span></div>
  </div>
  <div class="menu-box" style="left:40px;top:316px;width:408px;height:308px">
    <h3 class="box-title">Griechische Spezialitäten</h3>
    <div class="dish"><span class="dish-name">Kotopulo Gyros<span class="dish-desc">Hühnerfleisch gegrillt mit Pommes, Zatziki und Naturgemüse</span></span><span class="price">8,40</span></div>
    <div class="dish"><span class="dish-name">Kotopulo Stithos<span class="dish-desc">Hühnerbrust mit Reis, Zatziki und Naturgemüse</span></span><span class="price">8,20</span></div>
    <div class="dish"><span class="dish-name">Kotopulo Souvlaki<span class="dish-desc">Hühnerspieß mit Reis, Zatziki und Naturgemüse</span></span><span class="price">9,00</span></div>
    <div class="dish" style="width:250px"><span class="dish-name">Gyros<span class="dish-desc">Schweinefleisch mit Reis,<br>Tzatziki und Naturgemüse</span></span><span class="price">8,40</span></div>
    <div class="dish" style="width:210px"><span class="dish-name">Mix Souvlaki<span class="dish-desc">Huhn- und Schweinefleisch mit Reis,<br>Tzatziki und Naturgemüse</span></span><span class="price">9,00</span></div>
    <div class="dish" style="width:218px"><span class="dish-name">Paidakia<span class="dish-desc">Gegrilltes Lammkotelette mit Reis,<br>Tzatziki und Knoblauchsauce</span></span><span class="price">12,20</span></div>
  </div>
  <div class="illus" style="left:280px;top:555px;width:224px;height:90px" role="img" aria-label="Zeichnung eines gegrillten Steaks"></div>
  <footer class="footer-band"><span class="brand-name">Lorenzo</span></footer>
</section>

</body>
</html>
```